Visitenkarten-Design für Forschungs- und Beratungsunternehmen
Zielgruppe
*Veloricum' ist ein Forschungs- und Beratungsunternehmen für Lebensmittelwirkungen. Unsere Angebote sind: Vorträge, Workshops, Seminare und Coaching. Die Zielgruppen sind Pädagogen, Mediziner, Psychologen u.a.m.
Aufgabenstellung
Bei Bedarf kann die Gestaltung der Visitenkarte auch auf die Rückseite ausgedehnt werden.

```html
<!DOCTYPE html>
<html lang="de">
<head>
<meta charset="utf-8">
<title>Veloricum – Visitenkarte</title>
<link rel="stylesheet" href="https://fonts.googleapis.com/css2?family=Oswald:wght@400;500&family=Roboto+Condensed:wght@300;400&display=swap">
<style>
  :root {
    --bg: #161616;
    --card: #262626;
    --card-edge: #303030;
    --text: #f2f2f2;
    --muted: #b5b5b5;
    --orange: #f07a12;
    --blue: #1f8fd6;
    --green: #5fb526;
    --purple: #a23cb8;
  }
  * { margin: 0; padding: 0; box-sizing: border-box; }
  html, body { width: 1200px; height: 901px; overflow: hidden; background: var(--bg); }
  .stage {
    position: relative; width: 1200px; height: 901px;
    display: flex; align-items: center; justify-content: center; gap: 60px;
  }
  .card {
    position: relative; width: 520px; height: 300px;
    background: var(--card);
    border: 1px solid var(--card-edge);
    box-shadow: 0 18px 40px rgba(0,0,0,.55);
    color: var(--text);
  }
  .card--front { display: flex; align-items: center; justify-content: center; gap: 16px; }
  .brand-dot { width: 22px; height: 22px; border-radius: 50%; background: var(--orange); }
  .brand-name {
    font-family: "Oswald", sans-serif; font-weight: 500;
    font-size: 46px; letter-spacing: 1px; color: var(--text);
  }
  .holder { position: absolute; left: 0; right: 0; top: 96px; text-align: center; }
  .holder__accent { width: 24px; height: 24px; border-radius: 50%; background: var(--orange); margin: 0 auto 10px; }
  .holder__name { font-family: "Oswald", sans-serif; font-weight: 500; font-size: 24px; line-height: 1.1; }
  .holder__role { font-family: "Roboto Condensed", sans-serif; font-weight: 300; font-size: 14px; color: var(--muted); }
  .contact {
    position: absolute; display: flex; align-items: center; gap: 10px;
    font-family: "Roboto Condensed", sans-serif; font-weight: 400; font-size: 15px; color: var(--text);
  }
  .contact__icon {
    width: 24px; height: 24px; border-radius: 50%;
    display: flex; align-items: center; justify-content: center; flex: none;
  }
  .contact__icon svg { width: 13px; height: 13px; }
  .contact--phone { left: 34px; bottom: 40px; }
  .contact--phone .contact__icon { background: var(--green); }
  .contact--web { right: 34px; top: 150px; }
  .contact--web .contact__icon { background: var(--blue); }
  .contact--mail { right: 34px; bottom: 40px; }
  .contact--mail .contact__icon { background: var(--purple); }
</style>
</head>
<body>
<main class="stage">
  <section class="card card--front" aria-label="Vorderseite">
    <span class="brand-dot"></span>
    <span class="brand-name">Veloricum</span>
  </section>

  <section class="card card--back" aria-label="Rückseite">
    <div class="holder">
      <div class="holder__accent"></div>
      <div class="holder__name">Lukas Brenner</div>
      <div class="holder__role">Director</div>
    </div>

    <div class="contact contact--phone">
      <span class="contact__icon">
        <svg viewBox="0 0 24 24"><path fill="#fff" d="M6.6 10.8a15 15 0 0 0 6.6 6.6l2.2-2.2a1 1 0 0 1 1-.25 11.4 11.4 0 0 0 3.6.57 1 1 0 0 1 1 1V20a1 1 0 0 1-1 1A17 17 0 0 1 3 4a1 1 0 0 1 1-1h3.5a1 1 0 0 1 1 1c0 1.25.2 2.45.57 3.57a1 1 0 0 1-.25 1z"/></svg>
      </span>
      <span>+41 61 555 24 80</span>
    </div>

    <div class="contact contact--web">
      <span>www.veloricum.ch</span>
      <span class="contact__icon">
        <svg viewBox="0 0 24 24" fill="none" stroke="#fff" stroke-width="2"><circle cx="12" cy="12" r="9"/><path d="M3 12h18M12 3c3 3 3 15 0 18M12 3c-3 3-3 15 0 18"/></svg>
      </span>
    </div>

    <div class="contact contact--mail">
      <span>info@veloricum.ch</span>
      <span class="contact__icon">
        <svg viewBox="0 0 24 24" fill="none" stroke="#fff" stroke-width="2"><rect x="3" y="5" width="18" height="14" rx="1"/><path d="M3 6l9 7 9-7"/></svg>
      </span>
    </div>
  </section>
</main>
</body>
</html>
```